Poster Design for Film: 'Tres Lunas'

Tres Lunas means "two times" in Spanish. This short film is based on the true story of Cuban refugee during the take over of the Ordaz regime in 1959 and how is experiences and stories affected his children and grandchildren. Tres Lunas tells the story of Daniel- a recent grad who is forced to choose between his critically ill grandfather, the business opportunity of a lifetime, and maintaining a relationship with his love interest, Margaret. Through his grandfather's recollections as a young man in 1950's Cuba, Daniel gains a new outlook on life and the things that matter most.

This poster should evoke the drama and truth that the film approaches in a cinematic manner while maintaining the influences of true Cuban culture and history as perceived by a Miami audience today.

For more information please take a look at our fund raising site:
http://www.fundhaven.example/projects/tres-lunas

The grandfather's current life (the Cuban revolutionary/refugee as an old man):
www.clipvault.example/41592867
password: treslunas

A quick teaser of the film, exploring the lives of Daniel (the protagonist; grandson to Cuban refugee/revolutionary) and Meg (Daniel's love interest he neglects to commit to):

http://www.streamtube.example/watch?v=QbRtPwXnLeK

Please let me know if you would like any stills of the film, have any questions, etc. Thanks!

Hey all! So sorry for the delay on the stills- we had some serious technical issues, but now they are up!

Please let me know if you have any questions. We'll be uploaded more stills to choose from tonight.

Thanks!

Hey all!
Unless you need something in specific, I have just uploaded the final stills for the poster. Feel free to use any of the images, but please keep in mind that the main characters are Dan (the grandson), and his grandfather Arturo both young and old. In other words- the three guys.

Please let me know if you have any questions. Thanks! 

Here are some small text details for the bottom of the poster:

A Copper Lantern Production in association with BrightKiln Studios and the Coastal Pines University. Starring Brett Solano, Celina Fuentes, Omar Bustillo, Lucia Ortega, Farid Khoury. Written, Directed, & Produced by Marcos Ibarra. Director of Photography Tomas Varela. Edited by Marcos Ibarra & Tomas Varela.

Hey designers!

I've just uploaded a new still of the main character. Please try to include it in your design, as it is preferred over the other stills of the main character.

Thanks!

I've just uploaded two small logos to be featured on the bottom of the poster.

Thanks!

Target Market(s)

Hollywood. Cuban-Americans. Miamians. Film Critics. Students. Professors.

Adults based in Los Angeles and Miami aged 21-50 that speak English and Spanish and are in the art and entertainment industry.

Industry/Entity Type

Business

Requirements
Must have
• Must evoke the style of Cuba in the late 1950's while staying true to current day culture/style for 20-somethings in America (specifically LA, NYC, Miami).
Nice to have
• A sort of serious, almost stoic style that could possibly evoke a melancholic reaction.
Should not have
• Anything that evokes a daytime soap opera.

```html
<!DOCTYPE html>
<html lang="en">
<head>
<meta charset="utf-8">
<title>Tres Lunas — Film Poster</title>
<link href="https://fonts.googleapis.com/css2?family=Bebas+Neue&display=swap" rel="stylesheet">
<style>
  :root {
    --paper: #f1efea;
    --poster-red: #e42f26;
    --shadow-deep: #1f0504;
    --shadow-mid: #4a0c09;
    --ink-white: #ffffff;
  }
  * { margin: 0; padding: 0; box-sizing: border-box; }
  html, body {
    width: 800px; height: 1200px; overflow: hidden;
    background: var(--paper);
  }
  .poster {
    position: relative; width: 800px; height: 1200px;
    background: var(--paper);
    font-family: "Bebas Neue", "Oswald", sans-serif;
    color: var(--ink-white);
  }
  .poster-field {
    position: absolute; left: 33px; top: 33px; width: 734px; height: 1132px;
    background: var(--poster-red);
    overflow: hidden;
  }
  .portrait-silhouette {
    position: absolute; left: 115px; top: 45px; width: 500px; height: 940px;
    border-radius: 46% 46% 40% 40% / 22% 22% 30% 30%;
    background: radial-gradient(ellipse 55% 60% at 55% 42%, var(--shadow-deep) 0%, var(--shadow-deep) 55%, var(--shadow-mid) 78%, rgba(228,47,38,0) 100%);
  }
  .title {
    position: absolute; right: 411px; top: 438px;
    text-align: right; font-size: 148px; line-height: 122px;
    letter-spacing: 1px; text-transform: uppercase;
  }
  .cast-list {
    position: absolute; right: 411px; top: 734px;
    list-style: none; text-align: right;
    font-size: 34px; line-height: 40px; text-transform: uppercase;
  }
  .credit-block {
    position: absolute; left: 380px; top: 660px; width: 320px;
  }
  .credit-label { font-size: 22px; line-height: 24px; }
  .director-name { font-size: 50px; line-height: 48px; margin-top: 2px; }
  .synopsis {
    margin-top: 8px; font-size: 14.6px; line-height: 17.6px;
    text-transform: uppercase; letter-spacing: 0.1px;
  }
</style>
</head>
<body>
  <main class="poster">
    <section class="poster-field">
      <div class="portrait-silhouette" role="img" aria-label="Dark silhouette of the elderly grandfather in profile, head bowed, dissolving into smoke at the bottom"></div>

      <h1 class="title">Tres<br>Lunas</h1>

      <ul class="cast-list">
        <li>Brett Solano</li>
        <li>Celina Fuentes</li>
        <li>Omar Bustillo</li>
        <li>Lucia Ortega</li>
        <li>Farid Khoury</li>
      </ul>

      <div class="credit-block">
        <p class="credit-label">Directed by</p>
        <p class="director-name">Marcos Ibarra</p>
        <p class="synopsis">A short film is based on the true story of Cuban refugee during the take over of the Ordaz regime in 1959 and how is experiences and stories affected his children and grandchildren. Tres Lunas tells the story of Daniel- a recent grad who is forced to choose between his critically ill grandfather, the business opportunity of a lifetime, and maintaining a relationship with his love interest, Margaret. Through his grandfather's recollections as a young man in 1950's Cuba, Daniel gains a new outlook on life and the things that matter most.</p>
      </div>
    </section>
  </main>
</body>
</html>
```